Layout for site fence advertising - length approx. 250 cm x 125 cm

The advertising will later be printed on a PVC film and used for events or on sports fields.

Main services :
Your regional contact at
Real estate and business financing
independent insurance advice

```html
<!DOCTYPE html>
<html lang="en">
<head>
<meta charset="utf-8">
<title>Nordhaus Vermögensberatung – Fence Banner</title>
<link rel="stylesheet" href="https://fonts.googleapis.com/css2?family=Quicksand:wght@500;600&family=Saira+Condensed:wght@700&display=swap">
<style>
  :root {
    --brand-blue: #1a55b9;
    --band-grey: #5e5e5e;
    --text-grey: #4a4a4a;
    --white: #ffffff;
    --stage: #3d3d3d;
    --photo-dark: #4a3127;
    --photo-mid: #8a7468;
    --photo-light: #d9d4cf;
  }
  * { margin: 0; padding: 0; box-sizing: border-box; }
  html, body { width: 1000px; height: 1200px; overflow: hidden; }
  body {
    background: radial-gradient(ellipse at center, #5a5a5a 0%, var(--stage) 75%);
    position: relative;
  }
  .banner {
    position: absolute;
    left: 40px;
    top: 370px;
    width: 920px;
    height: 460px;
    background: var(--white);
    overflow: hidden;
    box-shadow: 0 12px 40px rgba(0,0,0,0.55);
  }
  .banner-shapes, .portrait-area {
    position: absolute;
    inset: 0;
    width: 920px;
    height: 460px;
  }
  .brand {
    position: absolute;
    left: 34px;
    top: 32px;
    display: flex;
    align-items: center;
    height: 118px;
  }
  .brand-dot {
    width: 26px;
    height: 26px;
    border-radius: 50%;
    background: var(--brand-blue);
    margin-right: 18px;
  }
  .brand-divider {
    width: 3px;
    height: 118px;
    background: var(--band-grey);
    margin-right: 12px;
  }
  .brand-text { display: flex; flex-direction: column; gap: 6px; }
  .brand-name {
    font-family: "Quicksand", sans-serif;
    font-weight: 600;
    font-size: 20px;
    color: var(--brand-blue);
    white-space: nowrap;
  }
  .brand-tagline {
    font-family: "Quicksand", sans-serif;
    font-weight: 500;
    font-size: 15.5px;
    color: var(--text-grey);
    white-space: nowrap;
  }
  .services {
    position: absolute;
    left: 34px;
    top: 196px;
    color: var(--white);
    font-family: "Saira Condensed", sans-serif;
    font-weight: 700;
    text-transform: uppercase;
  }
  .services-title {
    font-size: 40px;
    letter-spacing: 2.5px;
    line-height: 1;
    margin-bottom: 14px;
  }
  .services-list { list-style: none; }
  .services-list li {
    font-size: 25px;
    letter-spacing: 0.8px;
    line-height: 33px;
    display: flex;
    align-items: center;
  }
  .services-list li::before {
    content: "";
    width: 8px;
    height: 8px;
    border-radius: 50%;
    background: var(--white);
    margin-right: 8px;
  }
  .phone {
    position: absolute;
    left: 36px;
    top: 372px;
    font-family: "Saira Condensed", sans-serif;
    font-weight: 700;
    font-size: 74px;
    line-height: 86px;
    letter-spacing: 6px;
    color: var(--white);
  }
</style>
</head>
<body>
  <section class="banner">
    <svg class="banner-shapes" viewBox="0 0 920 460" aria-hidden="true">
      <rect class="services-band" x="0" y="175" width="920" height="191" fill="var(--brand-blue)"/>
      <rect class="phone-band" x="0" y="371" width="920" height="89" fill="var(--band-grey)"/>
      <path class="curve-gap" d="M 500 0 C 405 90 410 320 598 460 L 920 460 L 920 0 Z" fill="var(--white)"/>
      <path class="curve-accent" d="M 522 0 C 430 90 432 312 618 460 L 920 460 L 920 0 Z" fill="var(--brand-blue)"/>
    </svg>
    <svg class="portrait-area" viewBox="0 0 920 460" role="img" aria-label="Portrait photo of the financial advisor in a dark suit and white shirt, smiling, in a softly blurred office">
      <defs>
        <linearGradient id="portrait-tone" x1="0" y1="0" x2="1" y2="1">
          <stop offset="0" stop-color="var(--photo-light)"/>
          <stop offset="0.35" stop-color="var(--photo-mid)"/>
          <stop offset="1" stop-color="var(--photo-dark)"/>
        </linearGradient>
      </defs>
      <path d="M 578 0 C 488 80 470 300 652 460 L 920 460 L 920 0 Z" fill="url(#portrait-tone)" stroke="var(--white)" stroke-width="4"/>
    </svg>

    <div class="brand">
      <span class="brand-dot"></span>
      <span class="brand-divider"></span>
      <div class="brand-text">
        <span class="brand-name">Nordhaus Vermögensberatung GmbH</span>
        <span class="brand-tagline">Finanzieren, Versichern, Vorsorgen</span>
      </div>
    </div>

    <div class="services">
      <h2 class="services-title">Main Services :</h2>
      <ul class="services-list">
        <li>Your regional contact at</li>
        <li>Real estate and business financing</li>
        <li>Independent insurance advice</li>
      </ul>
    </div>

    <p class="phone">555-014-2270</p>
  </section>
</body>
</html>
```